Business Cards for a small business advisory (business services)

Professional look. Same as would apply for a lawyer, accountant, or other financial services professional. Please use the logo colors

Target Market(s)

small business owners

Industry/Entity Type

Financial Servics

Contact Information for Business Card

Name: Gavin L. Whitmore, CAIA / Title: Business Advisor / Office #: (718) 294-7716 / Mobile #: (917) 382-5047 / Email: g.whitmore@clearfieldventurepartners.example / Web: www.clearfieldventurepartners.example

Font styles to use
Sans Serif

```html
<!DOCTYPE html>
<html lang="en">
<head>
<meta charset="utf-8">
<title>Clearfield Venture Partners – Business Cards</title>
<link href="https://fonts.googleapis.com/css2?family=Montserrat:wght@400;500;600;700&display=swap" rel="stylesheet">
<style>
  :root {
    --navy: #15305f;
    --navy-deep: #10264d;
    --green: #6cb33f;
    --ink: #3a3d42;
    --paper: #f2f2f2;
    --backdrop: #d9dcdb;
  }
  * { box-sizing: border-box; margin: 0; padding: 0; }
  html, body {
    width: 1200px; height: 1200px; overflow: hidden;
    background: var(--backdrop);
    font-family: "Montserrat", sans-serif;
  }
  .sheet { position: relative; width: 1200px; height: 1200px; }
  .card {
    position: absolute; left: 150px; width: 900px; height: 514px;
    border-radius: 4px;
    box-shadow: 0 10px 30px rgba(0,0,0,0.18);
    overflow: hidden;
  }
  .card-front { top: 56px; background: linear-gradient(160deg, #f7f7f7, #e9e9e9); }
  .card-back  { top: 630px; }

  .brand-block {
    position: absolute; display: flex; flex-direction: column; align-items: flex-end;
  }
  .brand { display: flex; align-items: center; gap: 12px; }
  .brand-dot { width: 22px; height: 22px; border-radius: 50%; flex: none; background: var(--green); }
  .brand-name { font-weight: 600; font-size: 27px; letter-spacing: 0.2px; white-space: nowrap; }
  .brand-tagline {
    margin-top: 10px; font-weight: 700; font-size: 8.5px;
    letter-spacing: 0.2px; text-transform: uppercase; white-space: nowrap;
  }

  .card-front .brand-block { right: 60px; top: 58px; }
  .card-front .brand-name,
  .card-front .brand-tagline { color: var(--navy); }

  .person { position: absolute; left: 61px; top: 210px; }
  .person-name { font-weight: 700; font-size: 37px; color: var(--navy); letter-spacing: -0.3px; }
  .person-title { margin-top: 6px; font-weight: 400; font-size: 22px; color: var(--ink); }

  .contacts { position: absolute; left: 61px; top: 322px; list-style: none; }
  .contacts li {
    display: flex; align-items: center; gap: 12px;
    height: 36px; font-size: 22px; color: var(--ink);
  }
  .contacts svg { width: 19px; height: 19px; fill: var(--navy); flex: none; }
  .web-domain { color: var(--green); }

  .back-field {
    position: absolute; inset: 0;
    background: linear-gradient(180deg, #142d5a, #16336a);
  }
  .card-back .brand-block { right: 100px; top: 338px; }
  .card-back .brand-name,
  .card-back .brand-tagline { color: #ffffff; }
</style>
</head>
<body>
<main class="sheet">

  <section class="card card-front" aria-label="Business card front">
    <div class="brand-block">
      <div class="brand">
        <span class="brand-dot"></span>
        <span class="brand-name">Clearfield Venture Partners</span>
      </div>
      <p class="brand-tagline">Steady counsel for owners ready to buy or sell a small company</p>
    </div>

    <div class="person">
      <h1 class="person-name">Gavin L. Whitmore, CAIA</h1>
      <p class="person-title">Business Advisor</p>
    </div>

    <ul class="contacts">
      <li>
        <svg viewBox="0 0 24 24" aria-hidden="true"><path d="M6.6 10.8a15.1 15.1 0 0 0 6.6 6.6l2.2-2.2c.3-.3.7-.4 1-.2 1.1.4 2.3.6 3.6.6.6 0 1 .4 1 1V20c0 .6-.4 1-1 1A17 17 0 0 1 3 4c0-.6.4-1 1-1h3.5c.6 0 1 .4 1 1 0 1.3.2 2.5.6 3.6.1.3 0 .7-.2 1z"/></svg>
        <span>(718) 294-7716</span>
      </li>
      <li>
        <svg viewBox="0 0 24 24" aria-hidden="true"><path d="M7 1h10a2 2 0 0 1 2 2v18a2 2 0 0 1-2 2H7a2 2 0 0 1-2-2V3a2 2 0 0 1 2-2zm0 3v14h10V4zm5 15.5a1.2 1.2 0 1 0 0 2.4 1.2 1.2 0 0 0 0-2.4z"/></svg>
        <span>(917) 382-5047</span>
      </li>
      <li>
        <svg viewBox="0 0 24 24" aria-hidden="true"><path d="M2 5h20v14H2zm2 2.2v.3l8 5.2 8-5.2v-.3l-8 5.1z"/></svg>
        <span>g.whitmore@clearfieldventurepartners.example</span>
      </li>
      <li>
        <svg viewBox="0 0 24 24" aria-hidden="true"><path d="M12 2a10 10 0 1 0 0 20 10 10 0 0 0 0-20zm6.9 9h-3a15 15 0 0 0-1.3-5.6A8 8 0 0 1 18.9 11zM12 4.1c.9 1.2 1.8 3.6 1.9 6.9h-3.8c.1-3.3 1-5.7 1.9-6.9zM9.4 5.4A15 15 0 0 0 8.1 11h-3a8 8 0 0 1 4.3-5.6zM5.1 13h3a15 15 0 0 0 1.3 5.6A8 8 0 0 1 5.1 13zm6.9 6.9c-.9-1.2-1.8-3.6-1.9-6.9h3.8c-.1 3.3-1 5.7-1.9 6.9zm2.6-1.3a15 15 0 0 0 1.3-5.6h3a8 8 0 0 1-4.3 5.6z"/></svg>
        <span>www.<span class="web-domain">clearfieldventurepartners</span>.example</span>
      </li>
    </ul>
  </section>

  <section class="card card-back" aria-label="Business card back">
    <div class="back-field" role="img" aria-label="Navy field with a subtle repeating embossed star pattern"></div>
    <div class="brand-block">
      <div class="brand">
        <span class="brand-dot"></span>
        <span class="brand-name">Clearfield Venture Partners</span>
      </div>
      <p class="brand-tagline">Steady counsel for owners ready to buy or sell a small company</p>
    </div>
  </section>

</main>
</body>
</html>
```